Business Card

I need a business card for my work as an energy lawyer. I am a single prctioner and I consult to energy companies regarding a variety of legal issues involving environmental matters, energy efficiency, regulations and contractual arrangements. i need a distinctive business card that stands out and is easy to read. I like bold colors or high contrast. I like a sparse architectural design. The font should be easy to read (many of my clients use reading glasses and are concerned about small type). The card should communicate that I am somewhat different from ordinary legal counsel. Below are some examples of cards that I like. Thank you for your interest and thought. Glenn Dusty Harker
Updates

Thanks to everyone who has submitted a design.  My general comments are:

1.  I like the colourful cards and the high contrast cards.
2.  I prefer the use of icons for home address, phone, mobile and email.
3.  For the high contrast cards please use three colours - black background, and red and white for the logo or information.
4.  The mobile number area code should be 403 and not 404.
5.  I also need to add a direct phone line which is 403-517-6392.

Thank you,

Glenn Harker

Reason: I have briefly extended the deadline by three days to allow those individuals who responded early to revise their designs based upon the subsequent clarification of the colours (red, white, black background) and the request to use icons and add a direct phone number.

Industry/Entity Type

Business

```html
<!DOCTYPE html>
<html lang="en">
<head>
<meta charset="utf-8">
<title>Glenn Dusty Harker – Business Card</title>
<link href="https://fonts.googleapis.com/css2?family=Archivo+Black&family=Arimo:wght@400;700&display=swap" rel="stylesheet">
<style>
  :root {
    --backdrop: #e9e6e1;
    --card-red: #c4202b;
    --card-red-dark: #a8141e;
    --ink: #141414;
    --paper: #ffffff;
    --paper-shade: #ececec;
  }
  * { box-sizing: border-box; margin: 0; padding: 0; }
  html, body { width: 1200px; height: 900px; overflow: hidden; }
  body {
    background: var(--backdrop);
    font-family: "Arimo", Arial, sans-serif;
    position: relative;
  }
  .card {
    position: absolute;
    width: 560px;
    height: 320px;
    box-shadow: 0 6px 18px rgba(0,0,0,0.18);
    overflow: hidden;
  }
  .card-front {
    left: 80px; top: 100px;
    background: linear-gradient(135deg, var(--card-red), var(--card-red-dark));
    display: flex; align-items: center; justify-content: center;
  }
  .front-name {
    font-family: "Archivo Black", Arial, sans-serif;
    color: var(--ink);
    font-size: 30px;
    letter-spacing: 0.5px;
  }
  .card-back {
    left: 560px; top: 470px;
    background: linear-gradient(160deg, var(--paper) 40%, var(--paper-shade));
  }
  .identity {
    position: absolute; left: 150px; top: 40px;
    display: flex; align-items: center; gap: 10px;
  }
  .identity-mark {
    width: 26px; height: 26px; border-radius: 50%;
    background: var(--card-red);
  }
  .holder-name {
    font-family: "Archivo Black", Arial, sans-serif;
    font-size: 21px; color: var(--ink); line-height: 1;
  }
  .holder-title {
    font-size: 9px; font-weight: 700; color: var(--card-red);
    margin-top: 3px; text-align: right;
  }
  .contact-list {
    position: absolute; left: 300px; top: 118px;
    list-style: none;
  }
  .contact-item {
    display: flex; align-items: center; gap: 14px;
    font-size: 13px; font-weight: 700; color: var(--card-red);
    margin-bottom: 11px; line-height: 1.1;
  }
  .contact-icon { width: 18px; height: 18px; flex: none; }
  .corner-block {
    position: absolute; left: 0; bottom: 0;
    width: 200px; height: 150px;
    background: var(--card-red);
    display: flex; align-items: flex-end; padding: 0 0 16px 18px;
  }
  .corner-name {
    font-family: "Archivo Black", Arial, sans-serif;
    color: var(--paper); font-size: 24px; line-height: 1;
  }
</style>
</head>
<body>

<section class="card card-front" aria-label="Card front">
  <span class="front-name">Glenn Dusty Harker</span>
</section>

<section class="card card-back" aria-label="Card back">
  <div class="identity">
    <span class="identity-mark"></span>
    <div>
      <div class="holder-name">Glenn Dusty Harker</div>
      <div class="holder-title">Barrister and Solicitor, LLB, ICD.D</div>
    </div>
  </div>

  <ul class="contact-list">
    <li class="contact-item">
      <svg class="contact-icon" viewBox="0 0 18 18"><circle cx="9" cy="9" r="9" fill="#141414"/><path d="M5.5 5c1-1 1.6-.2 2 .6.3.6 0 1-.4 1.4.5 1.2 1.3 2 2.5 2.5.4-.4.8-.7 1.4-.4.8.4 1.6 1 .6 2-1.6 1.6-7.7-4.5-6.1-6.1z" fill="#fff"/></svg>
      <span>403-517-6392<br>1.403.628.1945</span>
    </li>
    <li class="contact-item">
      <svg class="contact-icon" viewBox="0 0 18 18"><circle cx="9" cy="9" r="9" fill="#141414"/><rect x="6" y="4" width="6" height="10" rx="1" fill="#fff"/><rect x="7" y="5.3" width="4" height="6" fill="#141414"/></svg>
      <span>1.403.835.2716</span>
    </li>
    <li class="contact-item">
      <svg class="contact-icon" viewBox="0 0 18 18"><circle cx="9" cy="9" r="9" fill="#141414"/><rect x="4.5" y="6" width="9" height="6.5" fill="#fff"/><path d="M4.5 6l4.5 3.6L13.5 6" fill="none" stroke="#141414" stroke-width="1"/></svg>
      <span>email: dusty@dustyharker.com</span>
    </li>
    <li class="contact-item">
      <svg class="contact-icon" viewBox="0 0 18 18"><circle cx="9" cy="9" r="9" fill="#141414"/><path d="M9 14.5s-3.5-4-3.5-6.3a3.5 3.5 0 017 0C12.5 10.5 9 14.5 9 14.5z" fill="#fff"/><circle cx="9" cy="8.2" r="1.3" fill="#141414"/></svg>
      <span>2875 Ridgeview Road S.W., Calgary, Alberta</span>
    </li>
  </ul>

  <div class="corner-block">
    <span class="corner-name">Glenn<br>Harker</span>
  </div>
</section>

</body>
</html>
```